Alaska Law Firm Needs a Sticker Design

We need a design for stickers to put on already-printed brochures. We mail the brochures to potential clients so they can learn more about accident-induced injuries, insurance claims, legal representation, and our own law firm.

One of our lawyers wrote a book that provides a helpful overview of personal injury claims. We are offering this book for free to anyone who calls and requests it. Therefore, the sticker design should include one of the following phrases, or something very similar:
a) "Still have questions? Call and request our book-- for free!"
b) "Still have questions about auto accident claims? Call and request our book today."
c) "Still have questions about filing a claim? Call and request a free copy of our book."
d) "Still have questions? Call us today to request a free copy of our book, Clear Lanes Ahead."
e) "To learn more about automobile accidents and insurance, call today and request a free copy of our book."

The sticker should be approximately 3"x3" and may be a circle, square, rectangle, or ellipsis. The sticker will be placed on the back of the folder, which is light blue. We would like the sticker to match the color scheme of our website and the folder.

I will upload an image of the book cover as soon as I obtain it.

Industry/Entity Type

Law Firm

Font styles to use
Serif
Sans Serif

Requirements
Should not have
• Bright colors that aren't already used in the folder design. e.g. no bright orange, pink, chartreuse, turquoise, yellow, red.

```html
<!DOCTYPE html>
<html lang="en">
<head>
<meta charset="utf-8">
<title>Free Book Sticker</title>
<link rel="stylesheet" href="https://fonts.googleapis.com/css2?family=Open+Sans:wght@300;400;600&display=swap">
<style>
  :root {
    --bg-light: #f4f4f4;
    --bg-mid: #d9d9d9;
    --navy: #0e3563;
    --slate: #5a5a5a;
    --steel: #2a5f9e;
    --face-core: #eef5fc;
    --face-edge: #bcd6ee;
    --white: #ffffff;
  }
  html, body {
    margin: 0;
    width: 1200px;
    height: 1200px;
    overflow: hidden;
    background: radial-gradient(circle at 50% 45%, var(--bg-light) 0%, var(--bg-mid) 100%);
  }
  .sticker {
    display: block;
    width: 1200px;
    height: 1200px;
    font-family: "Open Sans", Arial, sans-serif;
  }
  .t-navy { fill: var(--navy); }
  .t-slate { fill: #3d4f6a; }
  .t-accent { fill: var(--steel); }
  .t-white { fill: var(--white); }
  .w-light { font-weight: 300; }
  .w-reg { font-weight: 400; }
  .w-semi { font-weight: 600; }
  .call-label { font-family: "Open Sans", Arial, sans-serif; font-weight: 400; }
</style>
</head>
<body>
<svg class="sticker" viewBox="0 0 1200 1200" xmlns="http://www.w3.org/2000/svg">
  <defs>
    <radialGradient id="sticker-fill" cx="45%" cy="40%" r="65%">
      <stop offset="0%" stop-color="var(--face-core)"/>
      <stop offset="100%" stop-color="var(--face-edge)"/>
    </radialGradient>
  </defs>

  <!-- back rings -->
  <circle class="ring-grey" cx="570" cy="585" r="420" fill="var(--slate)"/>
  <circle class="ring-navy" cx="625" cy="620" r="425" fill="var(--navy)"/>
  <circle class="ring-gap" cx="590" cy="608" r="420" fill="var(--white)"/>
  <circle class="sticker-face" cx="590" cy="608" r="408" fill="url(#sticker-fill)"/>

  <!-- call icon -->
  <g class="call-icon">
    <path d="M262 560 c-22 10 -34 30 -30 55 c6 40 40 82 78 100 c22 10 44 4 56 -14 l-26 -28 c-10 8 -22 10 -32 2 c-16 -14 -28 -32 -34 -52 c-4 -12 2 -22 14 -28 z" fill="var(--navy)"/>
    <rect x="296" y="668" width="92" height="58" rx="8" fill="var(--navy)"/>
    <text class="call-label t-white" x="342" y="712" font-size="46" text-anchor="middle">call</text>
  </g>

  <!-- message -->
  <g class="message">
    <text x="364" y="379" class="t-navy"><tspan class="w-reg" font-size="52">"To learn </tspan><tspan class="w-reg" font-size="80">more</tspan></text>
    <text x="316" y="454" class="t-navy"><tspan class="w-reg" font-size="80">about </tspan><tspan class="w-reg t-slate" font-size="52">automobile</tspan></text>
    <text x="316" y="541"><tspan class="w-semi t-accent" font-size="92" letter-spacing="-2">accidents </tspan><tspan class="w-reg t-navy" font-size="52">and</tspan></text>
    <text x="416" y="626" class="t-navy w-reg" font-size="96">insurance,</text>
    <text x="405" y="694"><tspan class="w-semi t-accent" font-size="56">today </tspan><tspan class="w-light t-navy" font-size="56">and request</tspan></text>
    <text x="432" y="769" class="t-navy w-light" font-size="62">a free copy</text>
    <text x="343" y="858" class="t-navy w-reg" font-size="86">of our book."</text>
  </g>
</svg>
</body>
</html>
```